Design a Flyer for a carpet cleaning business. DOUBLE sided

I need a double sided flyer for a carpet cleaning business. You can just enter the front side for the contest then design a back if awarded the contest.

I want the flyer to look clean and fresh. I have attached a very rough layout as a pdf & ai file. I would like some variations on this theme and some design ideas. I have also uploaded the files from the ad plus some more.

I would like additional text on the flyer at the bottom as follows:

Friendly Local Carpet Cleaners | Fully Insured | Fully Trained | 100% Money Back Guarantee

Size is A5 w 15cm h 21.2

images not uploading http://www.meadowglowrugcare.co.uk/freelancer/ images here click on sandwich advert for pdf

```html
<!DOCTYPE html>
<html lang="en">
<head>
<meta charset="utf-8">
<title>Meadowglow Rug Care Flyer</title>
<link rel="stylesheet" href="https://fonts.googleapis.com/css2?family=Barlow+Semi+Condensed:wght@700&family=Barlow:wght@400;500;600;700&display=swap">
<style>
  :root {
    --ink: #111111;
    --orange: #f7a823;
    --yellow: #fdc10e;
    --white: #ffffff;
    --rule: #d9d9d9;
    --shadow: #cfcfcf;
    --rug-light: #f3ede2;
    --rug-mid: #e2d7c4;
    --rug-dark: #c9b9a0;
  }
  * { margin: 0; padding: 0; box-sizing: border-box; }
  html, body { width: 849px; height: 1200px; overflow: hidden; background: var(--white); }
  .flyer { position: relative; width: 849px; height: 1200px; background: var(--white); font-family: "Barlow", Arial, sans-serif; }

  .hero-photo {
    position: absolute; left: 0; top: 0; width: 849px; height: 584px;
    background: radial-gradient(ellipse at 55% 40%, var(--rug-light) 0%, var(--rug-mid) 60%, var(--rug-dark) 100%);
  }
  .hero-shadow { position: absolute; left: 0; top: 584px; width: 849px; height: 12px; background: linear-gradient(var(--shadow), var(--white)); }

  .headline {
    position: absolute; left: 34px; top: 626px;
    font-family: "Barlow Semi Condensed", "Arial Narrow", sans-serif; font-weight: 700;
    font-size: 92px; line-height: 1; letter-spacing: 0.5px; color: var(--ink); white-space: nowrap;
  }
  .headline .accent { color: var(--orange); }

  .selling-points { position: absolute; left: 273px; top: 728px; width: 394px; list-style: none; }
  .selling-points li {
    font-weight: 600; font-size: 26px; line-height: 45px; color: var(--ink);
    border-top: 1px solid var(--rule); white-space: nowrap;
  }
  .selling-points li:last-child { border-bottom: 1px solid var(--rule); }
  .selling-points .hl { color: var(--orange); }

  .pricing {
    position: absolute; left: 273px; top: 889px; width: 576px; height: 103px;
    background: var(--yellow); color: var(--white); padding: 8px 0 0 36px;
    box-shadow: 0 6px 0 var(--shadow);
  }
  .pricing .label { font-weight: 400; font-size: 23px; line-height: 29px; }
  .pricing .offer { font-weight: 600; font-size: 25px; line-height: 31px; white-space: nowrap; }

  .contact {
    position: absolute; left: 273px; top: 1017px; width: 576px; height: 116px;
    background: var(--orange); color: var(--white); padding: 8px 0 0 34px;
  }
  .contact .phone { font-weight: 700; font-size: 64px; line-height: 64px; letter-spacing: 2px; }
  .contact .email { font-weight: 500; font-size: 26px; line-height: 36px; }

  .website {
    position: absolute; left: 273px; top: 1141px; font-weight: 700; font-size: 30px;
    color: var(--orange); white-space: nowrap;
  }

  .brand { position: absolute; left: 36px; top: 1030px; width: 210px; text-align: center; }
  .brand svg { display: block; margin: 0 auto 10px; }
  .brand-name { font-weight: 700; font-size: 30px; line-height: 34px; color: var(--orange); }
</style>
</head>
<body>
<main class="flyer">
  <div class="hero-photo" role="img" aria-label="Photo of a young woman in a blue top and jeans relaxing on a clean cream shag carpet, wearing headphones, with a pillow and an open book"></div>
  <div class="hero-shadow"></div>

  <h1 class="headline">DIRTY <span class="accent">CARPETS?</span></h1>

  <ul class="selling-points">
    <li>Friendly <span class="hl">Local Carpet Cleaners</span></li>
    <li>Fully <span class="hl">Insured</span> | Fully <span class="hl">Trained</span></li>
    <li>100% <span class="hl">Money Back Guarantee</span></li>
  </ul>

  <section class="pricing">
    <p class="label">Simple Pricing:</p>
    <p class="offer">3 Rooms For £99</p>
    <p class="offer">Add Additional Rooms for £25 Per Room</p>
  </section>

  <section class="contact">
    <p class="phone">01632 960481</p>
    <p class="email">info@meadowglowrugcare.co.uk</p>
  </section>

  <p class="website">www.meadowglowrugcare.co.uk</p>

  <div class="brand">
    <svg width="60" height="60" viewBox="0 0 60 60" aria-hidden="true"><circle cx="30" cy="30" r="28" fill="#f7a823"/></svg>
    <p class="brand-name">Meadowglow<br>Rug Care</p>
  </div>
</main>
</body>
</html>
```